Vehicle Design Modern Company Vehicle

My new vehicle should be eye-catching and it should be immediately visible which company we are.
It should be modern and appealing. All pages can be printed.

The vehicle is a Varenne Courier New Model 2024 ( https://www.fahrzeugmarkt-beispiel.ch/auto/varenne-courier/7302519 ) Link is only a sample of the vehicle

The main eye-catcher of the foil should be the logo "basic logo chimney sweep. www.ofenputzmeister.li

The logo "Glutwerk" with the website www.glutwerkdienst.li should be kept discreet.

What I would like is if the lower third of the vehicle had roofs with chimneys/chimneys visible.

Our company is responsible for cleaning chimneys and combustion systems "chimney sweeps" and thus helps to save energy, prevent fires and protect the environment

Target Market(s)

Advertising on the vehicle

Colors

Designer to choose colors to be used in the design.

Requirements
Must have
• LogoName
Nice to have
• Good modern ideas

```html
<!DOCTYPE html>
<html lang="de">
<head>
<meta charset="utf-8">
<title>Kaminfeger Anstalt – Fahrzeugbeschriftung</title>
<link rel="stylesheet" href="https://fonts.googleapis.com/css2?family=Fira+Sans+Condensed:wght@600&family=Montserrat:wght@400&family=Bungee&family=Alfa+Slab+One&display=swap">
<style>
  :root{
    --teal:#1a8a85;
    --ink:#111111;
    --paper:#ffffff;
    --body:#f4f4f4;
    --body-line:#8a8a8a;
    --glass:#2a2a2a;
    --trim:#1c1c1c;
    --rim:#c4c4c4;
    --partner:#2c3d55;
    --sky-top:#3a3a3a;
    --sky-mid:#bdbdbd;
  }
  *{margin:0;padding:0;box-sizing:border-box}
  html,body{width:871px;height:1200px;overflow:hidden;background:var(--paper)}
  body{position:relative;font-family:"Montserrat",sans-serif;color:var(--ink)}

  .van{position:absolute;left:0;width:871px;height:377px}
  .van--left{top:0}
  .van--right{top:377px}

  .t{position:absolute;white-space:nowrap;line-height:1;text-align:center}
  .brand-mark{position:absolute;width:72px;height:72px;border:4px solid var(--ink);border-radius:50%}
  .brand-name{font-family:"Fira Sans Condensed",sans-serif;font-weight:600;font-size:23px;letter-spacing:.4px}
  .brand-owner{font-size:13px;letter-spacing:3.6px}
  .phone{font-family:"Bungee",sans-serif;color:var(--teal);font-size:35px}
  .web{font-family:"Alfa Slab One",serif;font-size:12px;letter-spacing:.3px}
  .partner-text{font-family:"Alfa Slab One",serif;font-size:5.5px;letter-spacing:.2px}
  .partner-dot{position:absolute;width:24px;height:24px;border:2px solid var(--partner);border-radius:50%}

  .rear{position:absolute;left:172px;top:790px;width:334px;height:334px;background:var(--ink);overflow:hidden}
  .rear-scene{position:absolute;left:0;top:0;width:334px;height:131px;background:linear-gradient(180deg,var(--sky-top) 0%,var(--sky-mid) 50%,#f0f0f0 100%)}
  .rear-band{position:absolute;left:0;top:131px;width:334px;height:118px;background:var(--teal);border-radius:10px 10px 0 0;color:var(--paper)}
  .rear-band .brand-mark{left:140px;top:11px;width:54px;height:54px;border:3px solid var(--paper)}
  .rear-band .brand-name{left:0;width:334px;top:73px;font-size:18px}
  .rear-rule{position:absolute;left:81px;top:93px;width:172px;height:1px;background:var(--paper)}
  .rear-band .brand-owner{left:0;width:334px;top:97px;font-size:9.5px;letter-spacing:2.8px}
  .rear-contact{position:absolute;left:0;top:249px;width:334px;height:66px;background:var(--paper);border-radius:0 0 12px 12px}
  .rear-contact .phone{left:0;width:334px;top:8px;font-size:34px}
  .rear-contact .web{left:0;width:334px;top:47px;font-size:11.5px}
  .rear .partner-dot{left:285px;top:12px;width:26px;height:26px}
  .rear .partner-text{left:240px;top:63px}

  .rear-caption{position:absolute;left:251px;top:1140px;width:200px;text-align:center;font-family:"Alfa Slab One",serif;font-size:13px;letter-spacing:.3px;line-height:1}
</style>
</head>
<body>

  <!-- Van, left side (front to the left) -->
  <svg class="van van--left" viewBox="0 0 1501 650" aria-label="Fahrzeugseite links">
    <defs>
      <symbol id="van-body" viewBox="0 0 1501 650">
        <path d="M120,380 C125,330 165,292 235,262 L390,180 C430,122 470,96 560,88 L1408,76 C1432,80 1442,110 1446,200 L1452,430 C1452,480 1444,508 1420,520 L1372,524 A112,112 0 0 0 1148,524 L372,530 A112,112 0 0 0 148,522 L126,516 Z" fill="var(--body)" stroke="var(--body-line)" stroke-width="3"/>
        <path d="M398,228 L478,124 C498,102 520,97 560,96 L722,95 L722,238 Z" fill="var(--glass)"/>
        <rect x="778" y="92" width="588" height="152" rx="24" fill="none" stroke="var(--body-line)" stroke-width="2"/>
        <line x1="746" y1="80" x2="746" y2="530" stroke="var(--body-line)" stroke-width="2"/>
        <line x1="402" y1="215" x2="410" y2="528" stroke="var(--body-line)" stroke-width="2"/>
        <rect x="645" y="285" width="70" height="14" rx="7" fill="var(--trim)"/>
        <path d="M150,275 C170,262 205,258 228,268 L215,300 C190,306 165,308 150,300 Z" fill="var(--trim)"/>
        <path d="M118,372 L170,372 L170,505 L128,505 C118,470 116,410 118,372 Z" fill="var(--trim)"/>
        <path d="M420,512 L1070,508 L1070,528 L420,532 Z" fill="var(--trim)"/>
        <rect x="1432" y="258" width="16" height="120" rx="4" fill="var(--trim)"/>
        <g>
          <circle cx="300" cy="515" r="78" fill="var(--trim)"/>
          <circle cx="300" cy="515" r="56" fill="var(--rim)"/>
          <circle cx="300" cy="515" r="14" fill="var(--trim)"/>
          <circle cx="1260" cy="522" r="78" fill="var(--trim)"/>
          <circle cx="1260" cy="522" r="56" fill="var(--rim)"/>
          <circle cx="1260" cy="522" r="14" fill="var(--trim)"/>
        </g>
      </symbol>
      <linearGradient id="roofs" x1="0" y1="0" x2="0" y2="1">
        <stop offset="0" stop-color="#111" stop-opacity="0"/>
        <stop offset=".35" stop-color="#111" stop-opacity=".55"/>
        <stop offset=".7" stop-color="#111" stop-opacity=".9"/>
        <stop offset="1" stop-color="#111"/>
      </linearGradient>
    </defs>
    <use href="#van-body"/>
    <rect role="img" aria-label="Silhouette eines Kaminfegers mit Besen auf Dächern mit rauchenden Kaminen" x="270" y="258" width="585" height="268" fill="url(#roofs)"/>
  </svg>

  <span class="brand-mark" style="left:585px;top:62px"></span>
  <div class="t brand-name" style="left:505px;width:232px;top:146px">KAMINFEGER ANSTALT</div>
  <div class="t brand-owner" style="left:505px;width:232px;top:178px">LORENZ VETTERLI</div>
  <div class="t phone" style="left:462px;width:320px;top:195px">+4 71 350 48 26</div>
  <div class="t web" style="left:465px;width:204px;top:236px">WWW.OFENPUTZMEISTER.LI</div>
  <div class="t partner-text" style="left:530px;top:267px">WWW.GLUTWERKDIENST.LI</div>
  <span class="partner-dot" style="left:628px;top:257px"></span>

  <!-- Van, right side (front to the right) -->
  <svg class="van van--right" viewBox="0 0 1501 650" aria-label="Fahrzeugseite rechts">
    <g transform="translate(1501,0) scale(-1,1)"><use href="#van-body"/></g>
    <rect role="img" aria-label="Silhouette eines Kaminfegers mit Besen auf Dächern mit rauchenden Kaminen und einem Vogel" x="718" y="262" width="395" height="275" fill="url(#roofs)"/>
  </svg>

  <span class="brand-mark" style="left:225px;top:437px"></span>
  <div class="t brand-name" style="left:144px;width:232px;top:521px">KAMINFEGER ANSTALT</div>
  <div class="t brand-owner" style="left:144px;width:232px;top:553px">LORENZ VETTERLI</div>
  <div class="t phone" style="left:102px;width:320px;top:571px">+4 71 350 48 26</div>
  <div class="t web" style="left:208px;width:204px;top:611px">WWW.OFENPUTZMEISTER.LI</div>
  <span class="partner-dot" style="left:230px;top:630px"></span>
  <div class="t partner-text" style="left:261px;top:643px">WWW.GLUTWERKDIENST.LI</div>

  <!-- Rear -->
  <section class="rear" aria-label="Heckansicht">
    <div class="rear-scene" role="img" aria-label="Kaminfeger-Silhouette mit Besen und Eimer auf einem Kamin vor Mond und Wolkenhimmel"></div>
    <span class="partner-dot"></span>
    <div class="t partner-text">WWW.GLUTWERKDIENST.LI</div>
    <div class="rear-band" role="img" aria-label="Dachlandschaft mit Kaminen in Türkis">
      <span class="brand-mark"></span>
      <div class="t brand-name">KAMINFEGER ANSTALT</div>
      <div class="rear-rule"></div>
      <div class="t brand-owner">LORENZ VETTERLI</div>
    </div>
    <div class="rear-contact">
      <div class="t phone">+4 71 350 48 26</div>
      <div class="t web">WWW.OFENPUTZMEISTER.LI</div>
    </div>
  </section>
  <div class="rear-caption">BACK OF CAR</div>

</body>
</html>
```